Personal Finance Author needs a postcard

Hi there,

I am a Canadian personal finance author and have published a new book called The Coin Keeper.

I teach Millennials how to create a 6-figure portfolio through investing (https://www.miradabbot.example/)

I'm speaking at some conferences so we were going to print some postcards to hand out to attendees with our info and calls-to-action on them.

I am looking for 4x6 (horizontal) postcard (no space needed for shipping label).

Logos, Headshots and Book Cover:
https://files.example.net/share/9ZqLp72WxTbVn4KcRd0sHj3aE5uYgMfo?view=open

Both sides will be full colour. I would like a clean and simple look. Our main sites are www.MiraDabbot.example and www.TheCoinKeeperBook.example if you want to get a sense of style and design.
I also uploaded a few marketing materials so you can see the existing designs.

Side 1:
Get Instant Access to your Free Resources - main headline

(small bullets underneath)
- The Coin Keeper Checklist
- Financial Worksheets
- Database of Investment Tools

MiraDabbot.example/Resources

At the bottom, include "Don't forget to follow Mira Dabbot on social media:
Linkedin: @miradabbot7
Facebook: @thecoinkeeperbook Instagram: @thecoinkeeperbook Twitter: @CoinKeeperBook"

Side 2:
Headline - Want to work directly with Mira and The Coin Keeper team to help you make your money grow and stay safe?

Work with us to (bullet point list)...
- Hire Mira as a Keynote Speaker
- Teach Financial Literacy Workshops
- Receive Financial Coaching

Want To Learn More About How We Can Help?
MiraDabbot.example/Services

Include my contact info:
Mira Dabbot
Author | Speaker | Investor
mira@thecoinkeeperbook.example
555-274-0381

Target Market(s)

Millennials who want to learn how to save and invest their money. I focus on stock market investing, real estate investing and entrepreneurship.

Industry/Entity Type

Financial Service

Font styles to use
Sans Serif

Colors

Designer to choose colors to be used in the design.

Requirements
Must have
• Photo of Mira Dabbot
• The Coin Keeper logo
• Green, Gold/Yellow to match existing colours
• modern business style postcard

```html
<!DOCTYPE html>
<html lang="en">
<head>
<meta charset="utf-8">
<title>The Coin Keeper – Conference Postcard</title>
<link rel="stylesheet" href="https://fonts.googleapis.com/css2?family=Saira+Semi+Condensed:wght@300;400;600;700;800&family=Montserrat:wght@800&display=swap">
<style>
  :root{
    --green:#0b6b2a;
    --green-dark:#075420;
    --ink:#111;
    --white:#fff;
    --paper-gray:#dcdcdc;
    --backdrop:#5b5b5b;
    --gold:linear-gradient(90deg,#b8860b 0%,#e6c46a 18%,#c4952a 38%,#fbe7ab 58%,#c99a2e 78%,#e8c876 100%);
  }
  *{box-sizing:border-box;margin:0;padding:0}
  html,body{width:1200px;height:1200px;overflow:hidden}
  body{background:var(--backdrop);position:relative;font-family:"Saira Semi Condensed",sans-serif;color:var(--ink)}
  .card{position:absolute;left:208px;width:784px;height:522px;overflow:hidden;background:var(--paper-gray)}
  .card--front{top:45px}
  .card--back{top:633px}
  .abs{position:absolute}
  .text-layer{z-index:2}
  .gold-band{background:var(--gold)}
  .green-rule{background:var(--green)}
  .tick{width:18px;height:18px;flex:none}
  ul{list-style:none}
  li{white-space:nowrap}

  /* front */
  .front-header{left:0;top:0;width:784px;height:126px;background:var(--white)}
  .front-top-stripe{left:0;top:0;width:784px;height:4px}
  .headline{right:32px;top:22px;text-align:right;white-space:nowrap}
  .headline__lead{font-weight:800;font-size:43px;line-height:46px;color:var(--green);letter-spacing:.3px}
  .headline__sub{font-weight:400;font-size:42px;line-height:46px;color:var(--ink)}
  .front-rule-top{left:0;top:124px;width:784px;height:5px}
  .front-gold{left:0;top:129px;width:784px;height:158px}
  .front-rule-bottom{left:0;top:286px;width:784px;height:4px}
  .resource-list{left:365px;top:148px}
  .resource-list li{display:flex;align-items:center;gap:16px;font-weight:600;font-size:24px;line-height:32px;color:#1a1a1a}
  .cta-pill{left:365px;top:264px;width:344px;height:44px;border-radius:22px;background:var(--green);color:var(--white);
    display:flex;align-items:center;justify-content:center;gap:12px;font-weight:300;font-size:22px;white-space:nowrap}
  .cta-shadow{left:395px;top:306px;width:284px;height:10px;border-radius:50%;background:radial-gradient(ellipse at center,rgba(0,0,0,.35),rgba(0,0,0,0) 70%)}
  .social{left:365px;top:342px}
  .social__title{font-weight:700;font-size:26px;line-height:32px;color:var(--green)}
  .social__rule{width:56px;height:2px;background:var(--green);margin:4px 0 8px}
  .social li{display:flex;align-items:center;gap:8px;font-size:16px;line-height:24.5px;color:#222}
  .social__dot{width:15px;height:15px;border-radius:50%;background:var(--green);flex:none}
  .divider-v{width:1px;background:#9a9a9a}
  .front-divider{left:572px;top:395px;height:90px}
  .book-mark{left:595px;top:382px;width:160px;text-align:center;color:var(--green);font-weight:700;font-size:36px;line-height:34px;text-transform:uppercase}
  .book-art{left:4px;top:14px;width:330px;height:488px;border-radius:6px;
    background:linear-gradient(160deg,#f4f4f1 0%,#e7e6e0 40%,#d6c07a 62%,#0b6b2a 78%,#f1efe8 100%)}
  .front-bottom-stripe{left:0;top:507px;width:784px;height:15px}

  /* back */
  .back-gold{left:0;top:0;width:784px;height:144px}
  .back-rule{left:0;top:143px;width:784px;height:6px}
  .pitch{right:32px;top:26px;text-align:right;white-space:nowrap}
  .pitch__line{font-size:27px;line-height:33px;color:var(--ink);font-weight:400}
  .pitch__line--strong{font-family:"Montserrat",sans-serif;font-weight:800;font-size:25px;letter-spacing:-.2px}
  .offer{top:164px}
  .offer--signup{left:362px}
  .offer--booking{left:568px}
  .offer__title{font-weight:700;font-size:20px;line-height:26px;color:var(--green)}
  .offer__rule{width:52px;height:2px;background:var(--green);margin:4px 0 8px}
  .offer li{display:flex;align-items:center;gap:10px;font-weight:600;font-size:16px;line-height:26px;color:#1a1a1a}
  .offer li .tick{width:17px;height:17px}
  .back-divider{left:548px;top:170px;height:100px}
  .contact-band{left:0;top:290px;width:784px;height:150px;background:var(--green)}
  .contact-band__lower{left:0;top:378px;width:784px;height:62px;background:var(--green-dark)}
  .contact-gold-line{left:0;top:440px;width:784px;height:5px}
  .contact{left:365px;top:297px;color:var(--white);white-space:nowrap}
  .contact__name{font-family:"Montserrat",sans-serif;font-weight:800;font-size:34px;line-height:42px;letter-spacing:.5px}
  .contact__role{font-weight:300;font-size:21px;line-height:28px}
  .contact__line{display:flex;align-items:center;gap:12px;font-weight:600;font-size:21px;line-height:31px}
  .contact__line svg{width:17px;height:17px;flex:none}
  .contact__first{margin-top:6px}
  .learn{right:32px;top:454px;text-align:right;white-space:nowrap}
  .learn__ask{font-weight:600;font-size:16px;line-height:22px;text-transform:uppercase;color:#1a1a1a}
  .learn__visit{font-size:16px;line-height:24px;color:#1a1a1a;display:flex;align-items:center;justify-content:flex-end;gap:6px}
  .learn__visit strong{font-weight:600}
  .learn__visit svg{width:15px;height:15px}
  .headshot{left:0;top:40px;width:322px;height:482px;z-index:1;
    clip-path:polygon(14% 14%,24% 3%,40% 0,56% 2%,68% 10%,72% 24%,72% 46%,82% 52%,94% 62%,100% 80%,100% 100%,0 100%,0 56%,8% 48%,10% 30%);
    background:linear-gradient(180deg,#6b4a36 0%,#c99a7c 30%,#e9c4aa 44%,#1c1c1c 60%,#141414 100%)}
  .back-bottom-stripe{left:0;top:510px;width:784px;height:12px;z-index:2}
</style>
</head>
<body>
<svg width="0" height="0" style="position:absolute" aria-hidden="true">
  <defs>
    <symbol id="icon-tick" viewBox="0 0 20 20">
      <path d="M17 9.5A7.5 7.5 0 1 1 12.5 3" fill="none" stroke="currentColor" stroke-width="2"/>
      <path d="M5.8 9.8l3.2 3.2 8.5-8.8" fill="none" stroke="currentColor" stroke-width="2.6" stroke-linecap="round" stroke-linejoin="round"/>
    </symbol>
  </defs>
</svg>

<!-- Front side -->
<section class="card card--front">
  <div class="abs front-header"></div>
  <div class="abs front-top-stripe gold-band"></div>
  <div class="abs front-rule-top green-rule"></div>
  <div class="abs front-gold gold-band"></div>
  <div class="abs front-rule-bottom green-rule"></div>

  <div class="abs book-art" role="img" aria-label="Stack of The Coin Keeper books by Mira Dabbot, cover showing the author holding a calculator"></div>

  <div class="abs headline text-layer">
    <div class="headline__lead">GET INSTANT ACCESS</div>
    <div class="headline__sub">To Your Free Resources</div>
  </div>

  <ul class="abs resource-list text-layer">
    <li><svg class="tick" style="color:var(--ink)"><use href="#icon-tick"/></svg>The Coin Keeper Checklists</li>
    <li><svg class="tick" style="color:var(--ink)"><use href="#icon-tick"/></svg>Financial Worksheets</li>
    <li><svg class="tick" style="color:var(--ink)"><use href="#icon-tick"/></svg>Database of Investment Tools</li>
  </ul>

  <div class="abs cta-shadow"></div>
  <div class="abs cta-pill text-layer">miradabbot.example/resources
    <svg width="16" height="18" viewBox="0 0 16 18" aria-hidden="true"><path d="M3 9l5 5 5-5M8 2v12" fill="none" stroke="#fff" stroke-width="2" stroke-linecap="round" stroke-linejoin="round"/></svg>
  </div>

  <div class="abs social text-layer">
    <div class="social__title">Let's Get Social</div>
    <div class="social__rule"></div>
    <ul>
      <li><span class="social__dot"></span>@miradabbot7</li>
      <li><span class="social__dot"></span>@CoinKeeperBook</li>
      <li><span class="social__dot"></span>@thecoinkeeperbook</li>
      <li><span class="social__dot"></span>@thecoinkeeperbook</li>
    </ul>
  </div>

  <div class="abs divider-v front-divider"></div>
  <div class="abs book-mark text-layer">The<br>Coin<br>Keeper</div>

  <div class="abs front-bottom-stripe gold-band"></div>
</section>

<!-- Back side -->
<section class="card card--back">
  <div class="abs back-gold gold-band"></div>
  <div class="abs back-rule green-rule"></div>

  <div class="abs pitch text-layer">
    <div class="pitch__line">Want to work directly with</div>
    <div class="pitch__line pitch__line--strong">MIRA AND THE COIN KEEPER TEAM</div>
    <div class="pitch__line">To Make Your Money Grow And Stay Safe?</div>
  </div>

  <div class="abs offer offer--signup text-layer">
    <div class="offer__title">SIGN UP FOR</div>
    <div class="offer__rule"></div>
    <ul>
      <li><svg class="tick" style="color:var(--green)"><use href="#icon-tick"/></svg>Wealth Workshops</li>
      <li><svg class="tick" style="color:var(--green)"><use href="#icon-tick"/></svg>Online Courses</li>
      <li><svg class="tick" style="color:var(--green)"><use href="#icon-tick"/></svg>Financial Coaching</li>
    </ul>
  </div>
  <div class="abs divider-v back-divider"></div>
  <div class="abs offer offer--booking text-layer">
    <div class="offer__title">BOOK MIRA AS A</div>
    <div class="offer__rule"></div>
    <ul>
      <li><svg class="tick" style="color:var(--green)"><use href="#icon-tick"/></svg>Keynote Speaker</li>
      <li><svg class="tick" style="color:var(--green)"><use href="#icon-tick"/></svg>Workshop Facilitator</li>
      <li><svg class="tick" style="color:var(--green)"><use href="#icon-tick"/></svg>Dynamic Panelist</li>
    </ul>
  </div>

  <div class="abs contact-band"></div>
  <div class="abs contact-band__lower"></div>
  <div class="abs contact-gold-line gold-band"></div>

  <div class="abs contact text-layer">
    <div class="contact__name">MIRA DABBOT</div>
    <div class="contact__role">Author | Speaker | Investor</div>
    <div class="contact__line contact__first">
      <svg viewBox="0 0 20 16" aria-hidden="true"><rect x="1" y="2" width="18" height="12" rx="1" fill="#fff"/><path d="M1.5 3l8.5 6 8.5-6" fill="none" stroke="var(--green-dark)" stroke-width="1.8"/></svg>
      mira@thecoinkeeperbook.example
    </div>
    <div class="contact__line">
      <svg viewBox="0 0 20 20" aria-hidden="true"><path d="M5 2l3 4-2 2c1 2.5 3.5 5 6 6l2-2 4 3-2 3C9 18 2 11 2 4z" fill="#fff"/></svg>
      555-274-0381
    </div>
  </div>

  <div class="abs learn text-layer">
    <div class="learn__ask">Want to learn more about how we can help?</div>
    <div class="learn__visit">Please Visit our Website:
      <svg viewBox="0 0 16 16" aria-hidden="true"><circle cx="8" cy="8" r="7" fill="none" stroke="#1a1a1a" stroke-width="1.4"/><ellipse cx="8" cy="8" rx="3" ry="7" fill="none" stroke="#1a1a1a" stroke-width="1.2"/><path d="M1 8h14M2.5 4.5h11M2.5 11.5h11" stroke="#1a1a1a" stroke-width="1.1"/></svg>
      <strong>miradabbot.example/services</strong>
    </div>
  </div>

  <div class="abs headshot" role="img" aria-label="Headshot of Mira Dabbot smiling, wearing a black blazer over a white top"></div>

  <div class="abs back-bottom-stripe gold-band"></div>
</section>
</body>
</html>
```